Halvercott Orthodontics business card

Using our existing logo (created with ArtFolio), please create a tasteful, contemporary business card. We are father and daughter orthodontists specializing in braces, clarafit, etc to design healthy, beautiful smiles for children, adolescents, and adults. We would like the design to be family-friendly but not childish.
The final design should include all of the information without looking cluttered (I hope! If necessary to achieve an optimal design, please consider making the card double-sided)
Purple, black, silver on a white card
Please include the following information:
Halvercott Orthodontics (logo)
Marguerite L. Halvercott, DMD
Douglas R. Halvercott, DMD

312 Bramblewood Street
North Andover, MA 01899
978.555.0142

847C Quarry Hollow Street
Methuen, MA 01898
978.555.0187

email frontdesk@halvercottortho.example
website www.halvercottortho.example

```html
<!DOCTYPE html>
<html lang="en">
<head>
<meta charset="utf-8">
<title>Halvercott Orthodontics — Business Card</title>
<link rel="stylesheet" href="https://fonts.googleapis.com/css2?family=Roboto+Condensed:wght@400;700&display=swap">
<style>
  :root {
    --purple: #6a2c96;
    --ink: #1c1c1c;
    --white: #ffffff;
    --stage: #e6e6e8;
  }
  * { box-sizing: border-box; margin: 0; padding: 0; }
  html, body {
    width: 1200px; height: 689px; overflow: hidden;
    background: var(--stage);
    font-family: "Roboto Condensed", "Arial Narrow", sans-serif;
  }
  .sheet {
    width: 1200px; height: 689px;
    display: flex; align-items: center; justify-content: center; gap: 40px;
  }
  .card {
    width: 540px; height: 309px;
    border-radius: 22px;
    position: relative;
    overflow: hidden;
    box-shadow: 0 6px 18px rgba(0,0,0,0.18);
  }
  .card--front {
    background: var(--purple);
    display: flex; align-items: center; justify-content: center;
  }
  .wordmark { display: flex; align-items: center; gap: 14px; }
  .wordmark__dot { width: 22px; height: 22px; border-radius: 50%; flex: none; }
  .wordmark__name {
    font-weight: 400;
    text-transform: uppercase;
    letter-spacing: 0.12em;
    white-space: nowrap;
  }
  .card--front .wordmark__dot { background: var(--white); }
  .card--front .wordmark__name { color: var(--white); font-size: 30px; }

  .card--back {
    background: var(--white);
    padding: 34px 30px 30px 38px;
  }
  .card--back .wordmark { gap: 10px; }
  .card--back .wordmark__dot { background: var(--purple); width: 16px; height: 16px; }
  .card--back .wordmark__name { color: var(--purple); font-size: 21px; }
  .doctors {
    margin-top: 28px;
    color: var(--purple);
    font-weight: 700;
    font-size: 25px;
    line-height: 1.12;
  }
  .contacts {
    margin-top: 22px;
    display: grid;
    grid-template-columns: auto auto;
    justify-content: space-between;
    column-gap: 18px;
  }
  .contact-list { list-style: none; }
  .contact-item {
    display: flex; align-items: flex-start; gap: 8px;
    color: var(--ink);
    font-size: 13px;
    line-height: 1.25;
    margin-bottom: 7px;
    white-space: nowrap;
  }
  .contact-item svg {
    width: 14px; height: 14px; flex: none; margin-top: 1px;
    fill: var(--purple);
  }
</style>
</head>
<body>
<main class="sheet">
  <section class="card card--front" aria-label="Card front">
    <div class="wordmark">
      <span class="wordmark__dot"></span>
      <span class="wordmark__name">Halvercott Orthodontics</span>
    </div>
  </section>

  <section class="card card--back" aria-label="Card back">
    <div class="wordmark">
      <span class="wordmark__dot"></span>
      <span class="wordmark__name">Halvercott Orthodontics</span>
    </div>

    <div class="doctors">
      <p>Marguerite L. Halvercott, DMD</p>
      <p>Douglas R. Halvercott, DMD</p>
    </div>

    <div class="contacts">
      <ul class="contact-list">
        <li class="contact-item">
          <svg viewBox="0 0 16 16" aria-hidden="true"><path d="M1 3h14v10H1z M1 3l7 6 7-6" fill="none" stroke="#6a2c96" stroke-width="1.6"/></svg>
          <span>frontdesk@halvercottortho.example</span>
        </li>
        <li class="contact-item">
          <svg viewBox="0 0 16 16" aria-hidden="true"><path d="M8 0a5.5 5.5 0 0 0-5.5 5.5C2.5 10 8 16 8 16s5.5-6 5.5-10.5A5.5 5.5 0 0 0 8 0zm0 7.8a2.3 2.3 0 1 1 0-4.6 2.3 2.3 0 0 1 0 4.6z"/></svg>
          <span>Ashbrook Office: 312 Bramblewood<br>Street Ashbrook, QX 01899</span>
        </li>
        <li class="contact-item">
          <svg viewBox="0 0 16 16" aria-hidden="true"><path d="M3.6 1l2.3 3.2-1.4 1.6a9 9 0 0 0 5.7 5.7l1.6-1.4L15 12.4 13.2 15C6.5 14.5 1.5 9.5 1 2.8z"/></svg>
          <span>555.555.0142</span>
        </li>
      </ul>
      <ul class="contact-list">
        <li class="contact-item">
          <svg viewBox="0 0 16 16" aria-hidden="true"><g fill="none" stroke="#6a2c96" stroke-width="1.4"><circle cx="8" cy="8" r="6.8"/><ellipse cx="8" cy="8" rx="3" ry="6.8"/><path d="M1.2 8h13.6M2.3 4.5h11.4M2.3 11.5h11.4"/></g></svg>
          <span>www.halvercottortho.example</span>
        </li>
        <li class="contact-item">
          <svg viewBox="0 0 16 16" aria-hidden="true"><path d="M8 0a5.5 5.5 0 0 0-5.5 5.5C2.5 10 8 16 8 16s5.5-6 5.5-10.5A5.5 5.5 0 0 0 8 0zm0 7.8a2.3 2.3 0 1 1 0-4.6 2.3 2.3 0 0 1 0 4.6z"/></svg>
          <span>Kellington Office: 847C Quarry Hollow<br>Street Kellington, QX 01898</span>
        </li>
        <li class="contact-item">
          <svg viewBox="0 0 16 16" aria-hidden="true"><path d="M3.6 1l2.3 3.2-1.4 1.6a9 9 0 0 0 5.7 5.7l1.6-1.4L15 12.4 13.2 15C6.5 14.5 1.5 9.5 1 2.8z"/></svg>
          <span>555.555.0187</span>
        </li>
      </ul>
    </div>
  </section>
</main>
</body>
</html>
```